Home Multi-Service Company Website

I currently have only a landing page but am looking for someone to build out a nice, modern looking website that will cover multiple services we offer like Landscape Lighting, Gutter Cleaning, Holiday Lighting, Window Cleaning, Insulation Services like Blow In and Removal, Blower Door Tests, Rodent Exclusion and Trapping and others. We would also like our Holiday lighting category to have links to a separate page for franchise opportunities.

Target Market(s)

Home

Font styles to use
Serif
Sans Serif

Requirements
Must have
• A modern and organized look. Detailed information regarding each service provided by our company.
Nice to have
• We are a service company so would like to see options to link reviews from quorvel and maybe some nice pictures of people at home. We would like the color to match our logo as well.

```html
<!DOCTYPE html>
<html lang="en">
<head>
<meta charset="utf-8">
<title>Hearthline Services</title>
<link rel="stylesheet" href="https://fonts.googleapis.com/css2?family=Righteous&family=Montserrat:ital,wght@0,300;0,400;0,500;0,600;0,700;1,300&display=swap">
<style>
:root{
  --navy:#2f3449;
  --ink:#1c1f2e;
  --white:#ffffff;
  --text-muted:#7d7f8a;
  --gold:#c9b24a;
  --hero-a:#2b3148;
  --hero-warm:#6b4a2c;
}
*{box-sizing:border-box;margin:0;padding:0}
html,body{width:1200px;height:2954px;overflow:hidden}
body{position:relative;font-family:"Montserrat",sans-serif;background:var(--white);color:var(--ink)}
.display{font-family:"Righteous",sans-serif;font-weight:400}
.btn{position:absolute;display:flex;align-items:center;justify-content:center;background:var(--ink);color:var(--white);font-family:"Montserrat",sans-serif;font-weight:500;text-transform:uppercase;text-decoration:none}

.hero{position:absolute;left:0;top:0;width:1200px;height:651px;background:linear-gradient(180deg,var(--hero-a) 0%,#3a3f58 55%,var(--hero-warm) 90%,#3a3428 100%)}
.hero-glow{position:absolute;left:0;top:0;width:1200px;height:651px;background:radial-gradient(ellipse 380px 160px at 880px 520px,rgba(230,160,80,.35),transparent 70%)}
.brand{position:absolute;left:143px;top:30px;color:var(--white);font-family:"Righteous",sans-serif;font-size:28px;line-height:30px}
.nav a{position:absolute;top:50px;color:var(--white);font-size:15px;font-weight:500;text-decoration:none;white-space:nowrap;text-transform:uppercase}
.nav .active{border-bottom:2px solid var(--white);padding-bottom:8px}
.hero-title{position:absolute;left:141px;top:268px;color:var(--white);font-size:74px;line-height:1}
.hero-sub{position:absolute;left:143px;top:377px;color:var(--white);font-size:26px;font-weight:700}

.services{position:absolute;left:0;top:651px;width:1200px;height:1085px;background:var(--navy)}
.section-title{position:absolute;left:142px;top:78px;color:var(--white);font-size:52px}
.card{position:absolute;width:441px;height:338px;display:flex;align-items:center;justify-content:center}
.card span{color:var(--white);font-weight:700;font-size:25px;text-transform:uppercase;text-shadow:0 1px 4px rgba(0,0,0,.4)}
.c-landscape{left:143px;top:183px;background:linear-gradient(160deg,#1f2a1c,#3f5a22 60%,#6e7f2a)}
.c-gutter{left:614px;top:183px;background:linear-gradient(160deg,#8a8a86,#5d6068 55%,#3e4a34)}
.c-holiday{left:143px;top:550px;background:linear-gradient(160deg,#15141a,#3b2f2a 55%,#2b4a3c)}
.c-window{left:614px;top:550px;background:linear-gradient(160deg,#9a9890,#5b4d40 55%,#7a7c80)}

.reviews{position:absolute;left:0;top:1736px;width:1200px;height:298px;background:var(--white)}
.quote{position:absolute;left:143px;top:72px;width:450px;font-size:15px;font-style:italic;font-weight:300;line-height:25px;color:var(--text-muted)}
.stars{position:absolute;left:143px;top:204px}
.about{position:absolute;left:681px;top:72px;width:400px;font-size:15px;font-weight:300;line-height:25px;color:var(--text-muted)}

.newsletter{position:absolute;left:0;top:2034px;width:1200px;height:625px;background:linear-gradient(180deg,#20261c 0%,#33402a 40%,#4a4434 70%,#6a5a48 100%)}
.news-title{position:absolute;left:0;width:1200px;top:200px;text-align:center;color:var(--white);font-size:55px;line-height:1}
.news-sub{position:absolute;left:0;width:1200px;top:280px;text-align:center;color:var(--white);font-size:20px}
.field{position:absolute;top:367px;width:223px;height:50px;background:var(--white);padding-left:30px;display:flex;align-items:center;font-size:11px;color:#555}

.footer{position:absolute;left:0;top:2659px;width:1200px;height:295px;background:var(--white)}
.footer-brand{position:absolute;left:143px;top:58px;font-family:"Righteous",sans-serif;font-size:40px;color:var(--navy)}
.footer-info{position:absolute;left:455px;top:60px;font-size:15.5px;font-weight:300;line-height:23px;color:var(--text-muted)}
.footer-links{position:absolute;left:770px;top:60px;font-size:15.5px;font-weight:300;line-height:26.5px;color:var(--text-muted);list-style:none}
.social{position:absolute;right:144px;top:62px;display:flex;gap:18px;font-size:14px;font-weight:600;color:var(--ink)}
.copy{position:absolute;left:0;width:1200px;top:222px;text-align:center;font-size:15.5px;font-weight:300;color:var(--text-muted)}
</style>
</head>
<body>

<header class="hero">
  <div class="hero-glow" role="img" aria-label="Modern two-storey house at dusk with lit windows and a wooden deck"></div>
  <div class="brand">Hearthline<br>Services</div>
  <nav class="nav">
    <a class="active" style="left:469px">Home</a>
    <a style="left:552px">Holiday Lighiting</a>
    <a style="left:739px">Services</a>
    <a style="left:849px">Reviews</a>
  </nav>
  <a class="btn" style="left:947px;top:39px;width:107px;height:40px;font-size:13px;font-weight:600">Book Now</a>
  <h1 class="hero-title display">Hearthline Services</h1>
  <p class="hero-sub">We are a Home Multi-Service Company</p>
  <a class="btn" style="left:143px;top:444px;width:172px;height:53px;font-size:16px">Book Now</a>
</header>

<section class="services">
  <h2 class="section-title display">What We Do</h2>
  <div class="card c-landscape" role="img" aria-label="Garden path lit by landscape lamps at night"><span>Landscape Lighting</span></div>
  <div class="card c-gutter" role="img" aria-label="Worker on a ladder cleaning a roof gutter"><span>Gutter Cleaning</span></div>
  <div class="card c-holiday" role="img" aria-label="House decorated with holiday string lights"><span>Holiday Lighting</span></div>
  <div class="card c-window" role="img" aria-label="Window being cleaned with a water-fed pole"><span>Window Cleaning</span></div>
  <a class="btn" style="left:143px;top:945px;width:171px;height:54px;font-size:16px">View More</a>
</section>

<section class="reviews">
  <p class="quote">“Lorem ipsum dolor sit amet, consecdipiscing elio eiusmod tempor incididunt ut ladoloreagna aliquuissuspendisse ultrices gravidasus commodo vimaecenas acc facilisisrem ipsum dolor sit amet, consectetur adipiscing”</p>
  <svg class="stars" width="95" height="14" viewBox="0 0 95 14" aria-label="Five stars">
    <g fill="var(--gold)">
      <polygon points="7,0 8.8,4.8 14,5 10,8.3 11.3,13.5 7,10.6 2.7,13.5 4,8.3 0,5 5.2,4.8"/>
      <polygon transform="translate(20 0)" points="7,0 8.8,4.8 14,5 10,8.3 11.3,13.5 7,10.6 2.7,13.5 4,8.3 0,5 5.2,4.8"/>
      <polygon transform="translate(40 0)" points="7,0 8.8,4.8 14,5 10,8.3 11.3,13.5 7,10.6 2.7,13.5 4,8.3 0,5 5.2,4.8"/>
      <polygon transform="translate(60 0)" points="7,0 8.8,4.8 14,5 10,8.3 11.3,13.5 7,10.6 2.7,13.5 4,8.3 0,5 5.2,4.8"/>
      <polygon transform="translate(80 0)" points="7,0 8.8,4.8 14,5 10,8.3 11.3,13.5 7,10.6 2.7,13.5 4,8.3 0,5 5.2,4.8"/>
    </g>
  </svg>
  <p class="about">Lorem ipsum dolor sit amet. consectetur adipiscing elied do eiusmod tempor incididunt ut ladoloreagna aliquuis ipsum suspendisse ultrices</p>
  <a class="btn" style="left:681px;top:175px;width:171px;height:54px;font-size:17px">Read More</a>
</section>

<section class="newsletter" role="img" aria-label="Garden walkway at night with bollard lights and flower beds">
  <h2 class="news-title display">Subscribe to Our Newsletter</h2>
  <p class="news-sub">Sign up to receive news and updates.</p>
  <div class="field" style="left:170px">First Name</div>
  <div class="field" style="left:405px">Last Name</div>
  <div class="field" style="left:639px">Email Address</div>
  <a class="btn" style="left:874px;top:367px;width:156px;height:50px;font-size:16px">Read More</a>
</section>

<footer class="footer">
  <div class="footer-brand">Hearthline</div>
  <div class="footer-info">123.Lorem ipsum dolor sit amet<br>consectetur adipiscing<br><span style="display:block;margin-top:12px">1 888 888 8888</span></div>
  <ul class="footer-links">
    <li>Home</li><li>Holiday lighting</li><li>Services</li><li>Reviews</li>
  </ul>
  <div class="social"><span>Friendnet</span><span>Photoloop</span></div>
  <p class="copy">© 2021 Hearthline Services. All rights reserved.Privacy Terms of Use</p>
</footer>

</body>
</html>
```